Clean, minimal label design needed for new skincare line.

Want clean, minimal labels for Clean (non-toxic), cosmeceutical grade Australian-made skincare products. We are going for a minimal and simple approach to our branding so want the labelling to follow suit. Please find logos attached below. Labels are white and logo is black. Font to be black, avoid colours other than white or black.

Target Market(s)

25-65+

Industry/Entity Type

Beauty

Requirements
Must have
• On the front:
- logo
- product name eg. moisturiser 1
- descriptive words eg. light
- weight eg. 30mls/1 fl oz

On the back:
- directions eg. apply one pump both AM and PM after serum application and prior to barrier protect application.
- Cruelty free icon
- Vegan icon
- Made in Australia Icon
- Open jar with 12M Icon
Nice to have
• See above
Should not have
• Avoid colours other than white or black.

```html
<!DOCTYPE html>
<html lang="en">
<head>
<meta charset="utf-8">
<title>fernlane co. skincare – moisturiser labels</title>
<link rel="stylesheet" href="https://fonts.googleapis.com/css2?family=Montserrat:wght@400;500;800&family=Playfair+Display:wght@800&family=Jost:wght@400;500&family=Allura&display=swap">
<style>
  :root {
    --ink: #111111;
    --paper: #ffffff;
    --backdrop: #ececec;
    --muted: #2a2a2a;
  }
  * { box-sizing: border-box; margin: 0; padding: 0; }
  html, body {
    width: 1200px;
    height: 1200px;
    overflow: hidden;
    background: var(--backdrop);
  }
  .canvas {
    width: 1200px;
    height: 1200px;
    display: flex;
    justify-content: center;
    align-items: center;
    gap: 80px;
  }
  .label {
    position: relative;
    width: 440px;
    height: 800px;
    background: var(--paper);
    color: var(--ink);
  }

  /* Front label */
  .brand {
    position: absolute;
    top: 70px;
    left: 0;
    right: 0;
    text-align: center;
  }
  .brand-name {
    font-family: "Montserrat", sans-serif;
    font-weight: 800;
    font-size: 44px;
    letter-spacing: -1.5px;
    line-height: 1;
  }
  .brand-line {
    font-family: "Montserrat", sans-serif;
    font-weight: 500;
    font-size: 24px;
    letter-spacing: 1px;
    margin-top: 10px;
  }
  .product {
    position: absolute;
    top: 450px;
    left: 55px;
    right: 55px;
    text-align: center;
  }
  .product-name {
    font-family: "Playfair Display", serif;
    font-weight: 800;
    font-size: 54px;
    line-height: 1;
    padding-bottom: 14px;
    border-bottom: 2px solid var(--ink);
  }
  .product-descriptor {
    font-family: "Allura", cursive;
    font-size: 58px;
    line-height: 1;
    margin-top: 10px;
  }
  .volume {
    position: absolute;
    top: 660px;
    left: 0;
    right: 0;
    display: flex;
    align-items: center;
    gap: 14px;
  }
  .volume::before, .volume::after {
    content: "";
    flex: 1;
    height: 4px;
    background: var(--ink);
  }
  .volume-text {
    font-family: "Montserrat", sans-serif;
    font-weight: 400;
    font-size: 24px;
  }

  /* Back label */
  .directions {
    position: absolute;
    top: 70px;
    left: 50px;
    right: 20px;
    font-family: "Jost", sans-serif;
    font-size: 29px;
    line-height: 1.5;
    color: var(--muted);
  }
  .directions-title {
    font-weight: 500;
    color: var(--ink);
  }
  .divider {
    position: absolute;
    top: 530px;
    left: 60px;
    right: 50px;
    height: 2px;
    background: var(--ink);
  }
  .badges {
    position: absolute;
    top: 580px;
    left: 60px;
    right: 40px;
    display: flex;
    justify-content: space-between;
    align-items: center;
  }
  .base-rule {
    position: absolute;
    top: 730px;
    left: 0;
    right: 0;
    height: 4px;
    background: var(--ink);
  }
</style>
</head>
<body>
  <main class="canvas">
    <section class="label label-front">
      <div class="brand">
        <div class="brand-name">fernlane co.</div>
        <div class="brand-line">skincare</div>
      </div>
      <div class="product">
        <h1 class="product-name">moisturiser</h1>
        <div class="product-descriptor">light</div>
      </div>
      <div class="volume"><span class="volume-text">30 mls/1 fl.oz.</span></div>
    </section>

    <section class="label label-back">
      <div class="directions">
        <p class="directions-title">DIRECTIONS:</p>
        <p>Apply one pump both<br>AM and PM after serum<br>application and prior to<br>barrier protect application.</p>
      </div>
      <div class="divider"></div>
      <div class="badges">
        <svg class="badge" width="76" height="76" viewBox="0 0 76 76" role="img" aria-label="Vegan badge">
          <circle cx="38" cy="38" r="34" fill="none" stroke="#111" stroke-width="4"/>
        </svg>
        <svg class="badge" width="76" height="76" viewBox="0 0 76 76" role="img" aria-label="Cruelty free badge">
          <path d="M38 66 L10 36 A15 15 0 0 1 38 16 A15 15 0 0 1 66 36 Z" fill="none" stroke="#111" stroke-width="4"/>
        </svg>
        <svg class="badge" width="92" height="76" viewBox="0 0 92 76" role="img" aria-label="Australian made badge">
          <polygon points="46,6 88,70 4,70" fill="#111"/>
        </svg>
        <svg class="badge" width="66" height="76" viewBox="0 0 66 76" role="img" aria-label="Period after opening badge">
          <rect x="8" y="30" width="50" height="38" rx="3" fill="none" stroke="#111" stroke-width="3"/>
          <line x1="6" y1="22" x2="46" y2="6" stroke="#111" stroke-width="3"/>
        </svg>
      </div>
      <div class="base-rule"></div>
    </section>
  </main>
</body>
</html>
```